Design for "Vellow" protein health bars wrappers

I need a new design for a protein bar that my partners and I are launching for the North American and European markets.
The bar's name is "Vellow."
Given the masculine/aggressive nature of that name, we are thinking of neutralizing it with a more feminine/soft font and design. But hey - the sky is the limit. We obviously want this 20-gram protein bar to sell to a wide net (not just men but women also). So if it means having a Pellam Comic font/design (or whatever) in order to do this, so be it. I leave it up to your intelligence and experience.

ADDED ON FEBRUARY 24:

The official name of the bar is just "VELLOW" (not "Vellow Protein").

We have six flavors divided into two categories, which are 1) SOFT and 2) CRUNCHY.
So, the idea is to make two similar designs for the wrapper that still distinguish themselves from each other because one is 'soft' and the other is 'crunchy.'
Then, within each category, the idea is to have three color variations, designating the three flavors in each category.

Please look at the dimensions and examples of the generic wrapper designs that we already have (and which we find too generic), which I have uploaded.

Target Market(s)

North America - Brindle, Fair Harvest
Europe - Norway, Sweden, Denmark, Germany, France, Switzerland, Italy.

Industry/Entity Type

Nutrition

Logo Text

Vellow

Font styles to use
Serif
Decorative

Colors
fff6dc
f04a50

Requirements
Must have
• The title is "Vellow".
• We have six flavors divided into two categories, which are 1) SOFT and 2) CRUNCHY.
• You can work on the two different types of similar-but-different designs for the "soft" and for the "cruncy." Then it's just a question of color variations for each flavor.
• The flavors are:
• SOFT: 1) strawberry, 2) Chocolate brownie, 3) Cinnamon Crunch
• CRUNCY: 1) Peanut, 2) Lemon, 3) Coconut.
• On the side or at the bottom, there should be stated:
• "20 gm protein"
• "children friendly"
Nice to have
• Obvious: a design that catches the eye and inspires someone to buy the bar to eat it.
• Part of the design could include a photograph of the actual bar (you can use generic photos for that until we place a pic of the actual bar). Like 1/4th of the total surface (or even a little smaller).

```html
<!DOCTYPE html>
<html lang="en">
<head>
<meta charset="utf-8">
<title>Vellow Protein Bar Wrappers</title>
<link href="https://fonts.googleapis.com/css2?family=Anton&family=Archivo:wght@700;800&family=Yellowtail&family=Great+Vibes&display=swap" rel="stylesheet">
<style>
  :root {
    --backdrop: #a89c86;
    --silver-light: #f4f4f2;
    --silver-dark: #c9c7c2;
    --gold: #d8a22c;
    --gold-deep: #b9831c;
    --gold-band: #7a5414;
    --brown-text: #6b2a10;
    --red: #b3121c;
    --red-deep: #8e0d15;
    --red-band: #6f0e12;
    --red-script: #c8141e;
    --white: #ffffff;
    --ink: #2a1a10;
  }
  * { margin: 0; padding: 0; box-sizing: border-box; }
  html, body { width: 1200px; height: 1200px; overflow: hidden; }
  body { background: var(--backdrop); position: relative; }

  .wrapper {
    position: absolute;
    left: 80px;
    width: 1040px;
    height: 320px;
    overflow: hidden;
    box-shadow: 0 14px 30px rgba(40, 30, 20, 0.35);
  }
  .wrapper--crunchy { top: 200px; }
  .wrapper--chewy { top: 630px; }

  .band { position: absolute; left: 0; width: 100%; }
  .band--top {
    top: 0; height: 80px;
    background: linear-gradient(180deg, var(--silver-light), var(--silver-dark));
  }
  .band--main { top: 80px; height: 170px; }
  .band--bottom { top: 250px; height: 70px; display: flex; align-items: center; justify-content: center; }

  .wrapper--crunchy .band--main { background: linear-gradient(180deg, var(--gold), var(--gold-deep)); }
  .wrapper--crunchy .band--bottom { background: var(--gold-band); }
  .wrapper--chewy .band--main { background: linear-gradient(180deg, var(--red), var(--red-deep)); }
  .wrapper--chewy .band--bottom { background: var(--red-band); }

  .seal {
    position: absolute; top: 0; width: 40px; height: 100%;
    background: repeating-linear-gradient(180deg, rgba(255,255,255,0.18) 0 4px, rgba(0,0,0,0.08) 4px 8px);
  }
  .seal--left { left: 0; }
  .seal--right { right: 0; }

  .variant {
    position: absolute; left: 90px; top: 6px;
    font-size: 58px; line-height: 1;
  }
  .wrapper--crunchy .variant { font-family: "Great Vibes", cursive; color: var(--ink); }
  .wrapper--chewy .variant { font-family: "Yellowtail", cursive; color: var(--red-script); }

  .brand {
    position: absolute; left: 96px; top: 58px;
    font-family: "Anton", sans-serif;
    font-size: 168px; line-height: 1;
    color: var(--white);
    letter-spacing: 2px;
    text-shadow: 4px 5px 0 rgba(0, 0, 0, 0.35);
  }

  .bar-photo {
    position: absolute; left: 640px; top: 70px;
    width: 180px; height: 190px;
    border-radius: 10px;
  }
  .wrapper--crunchy .bar-photo { background: radial-gradient(circle at 45% 40%, #6a3a22, #3a1d10); }
  .wrapper--chewy .bar-photo { border-radius: 50% 50% 46% 46%; background: radial-gradient(circle at 40% 40%, #f0383e, #a80d16); }

  .flavour {
    position: absolute; left: 836px; top: 108px; width: 160px;
    font-family: "Archivo", sans-serif; font-weight: 800;
    font-size: 23px; line-height: 1.12; text-align: center;
  }
  .flavour__amount { font-size: 34px; display: block; }
  .wrapper--crunchy .flavour { color: var(--brown-text); }
  .wrapper--chewy .flavour { color: var(--white); }

  .tagline {
    font-family: "Archivo", sans-serif; font-weight: 700;
    font-size: 20px; letter-spacing: 1.5px;
    color: var(--white);
    word-spacing: 6px;
  }
  .wrapper--crunchy .tagline { color: #f3d58a; }
</style>
</head>
<body>

  <section class="wrapper wrapper--crunchy" aria-label="Crunchy chocolate brownie wrapper">
    <div class="band band--top"></div>
    <div class="band band--main"></div>
    <div class="band band--bottom">
      <p class="tagline">SMOOTH PROTEIN EASILY DIGESTED SUITABLE FOR CHILDREN</p>
    </div>
    <div class="seal seal--left"></div>
    <div class="seal seal--right"></div>
    <span class="variant">Crunchy</span>
    <h1 class="brand">VELLOW</h1>
    <div class="bar-photo" role="img" aria-label="Photo of stacked chocolate brownie pieces"></div>
    <p class="flavour"><span class="flavour__amount">20g</span>CHOCOLATE BROWNIE PROTEIN BAR</p>
  </section>

  <section class="wrapper wrapper--chewy" aria-label="Chewy strawberry wrapper">
    <div class="band band--top"></div>
    <div class="band band--main"></div>
    <div class="band band--bottom">
      <p class="tagline">SMOOTH PROTEIN EASILY DIGESTED CHILDREN FRIENDLY</p>
    </div>
    <div class="seal seal--left"></div>
    <div class="seal seal--right"></div>
    <span class="variant">Chewy</span>
    <h2 class="brand">VELLOW</h2>
    <div class="bar-photo" role="img" aria-label="Photo of a ripe strawberry with green leaves"></div>
    <p class="flavour"><span class="flavour__amount">20 G</span>STRAWBERRY PROTEIN BAR</p>
  </section>

</body>
</html>
```